Design for a 4 screens iOS and Android app - "TrajiMesur"

The app allows you to track your car gasoline refill ...
We need a design for the 4 screens of the app:
a) 1 form with 3 fields.
b) 1 simple list view
c) 1 summary view
d) 1 text page
2 "alerts" items are also to be designed.
No specific guidelines, nor logo or whatever.
It will be a free app distributed on iOS and Androïd.
We just want to make it looking nice & very usable for end users.
Target Market(s)
B2C app
Industry/Entity Type
Android

```html
<!DOCTYPE html>
<html lang="en">
<head>
<meta charset="utf-8">
<title>TrajiMesur – Data saved</title>
<link rel="stylesheet" href="https://fonts.googleapis.com/css2?family=Roboto:wght@400;700;900&display=swap">
<style>
  :root {
    --tab-bg: #3a9ff2;
    --tab-divider: #b9dcf8;
    --icon: #c4e2f8;
    --screen-top: #79bde9;
    --screen-bottom: #4a8fcf;
    --field-bg: #bde0f4;
    --field-text: #8fb1c9;
    --alert-bg: #ffffff;
    --accent: #0a86f7;
    --save-bg: #3a9ff2;
    --save-text: #c6e3f8;
    --link-text: #bde0f4;
  }
  * { box-sizing: border-box; margin: 0; padding: 0; }
  html, body { width: 675px; height: 1200px; overflow: hidden; }
  body {
    font-family: "Roboto", Arial, sans-serif;
    position: relative;
    background: linear-gradient(to bottom, var(--screen-top) 0, var(--screen-top) 700px, var(--screen-bottom) 1200px);
  }
  .tab-bar {
    position: absolute; top: 0; left: 0; width: 675px; height: 107px;
    display: flex; background: var(--tab-bg);
  }
  .tab {
    flex: 1; display: flex; align-items: center; justify-content: center;
    border-right: 1px solid var(--tab-divider);
  }
  .tab:last-child { border-right: none; }
  .amount-field {
    position: absolute; left: 85px; top: 364px; width: 505px; height: 81px;
    background: var(--field-bg); border-radius: 18px;
    padding-left: 50px; display: flex; align-items: center;
    font-size: 34px; font-weight: 700; color: var(--field-text);
  }
  .alert {
    position: absolute; left: 0; top: 482px; width: 675px; height: 223px;
    background: var(--alert-bg); text-align: center;
  }
  .alert-title {
    margin-top: 56px; font-size: 31px; font-weight: 700; color: var(--accent);
  }
  .alert-button {
    display: block; margin: 32px auto 0; width: 172px; height: 57px;
    background: var(--accent); border-radius: 13px; border: none;
    color: #fff; font: 700 25px "Roboto", Arial, sans-serif;
  }
  .save-button {
    position: absolute; left: 197px; top: 791px; width: 282px; height: 85px;
    background: var(--save-bg); border-radius: 20px; border: none;
    color: var(--save-text); font: 900 33px "Roboto", Arial, sans-serif;
  }
  .about-link {
    position: absolute; left: 0; width: 675px; top: 1064px; text-align: center;
    font-size: 27px; color: var(--link-text);
  }
</style>
</head>
<body>
  <nav class="tab-bar">
    <div class="tab">
      <svg width="46" height="46" viewBox="0 0 46 46" aria-label="Add refill">
        <path d="M23 2v42M2 23h42" stroke="var(--icon)" stroke-width="3.5" stroke-linecap="round"/>
      </svg>
    </div>
    <div class="tab">
      <svg width="64" height="46" viewBox="0 0 64 46" aria-label="Refill list">
        <g fill="var(--icon)"><circle cx="5" cy="5" r="4.5"/><circle cx="5" cy="23" r="4.5"/><circle cx="5" cy="41" r="4.5"/></g>
        <g stroke="var(--icon)" stroke-width="3.5" stroke-linecap="round"><path d="M21 5h40M21 23h40M21 41h40"/></g>
      </svg>
    </div>
    <div class="tab">
      <svg width="60" height="46" viewBox="0 0 60 46" aria-label="Summary">
        <path d="M3 2v42h55" fill="none" stroke="var(--icon)" stroke-width="3.5" stroke-linecap="round"/>
        <path d="M9 37V24l5-5 7 6 9-11 12 12 10 11z" fill="var(--icon)"/>
      </svg>
    </div>
  </nav>

  <div class="amount-field">127500</div>

  <div class="alert" role="alertdialog">
    <p class="alert-title">Data saved</p>
    <button class="alert-button">OK</button>
  </div>

  <button class="save-button">Save</button>

  <p class="about-link">About us</p>
</body>
</html>
```